Verdale Landscape & Design Website Design

We are working with a Gardening & Landscape Design company in California. They provide residential and commercial gardening services throughout California.

Some sites to use for inspiration:
https://plotmerra.example
https://www.quenvaleterra.example
https://www.mossbrinkvo.example
https://www.tillowmarsh.example

Thank you for taking the time to consider designing a website for us. We are web developers based in Stockton, CA, USA. Most of our projects go through the same process. Understanding this process may help you win a project with us. We custom-code all of our websites in-house. We don’t have any requirements as to what tools you use for your design, but we ask that you follow these guidelines.

IMAGES:
If you use any images or icons in the design, we ask that you have a link to the asset so we can purchase the image/icon. Most of the designs we submit do not have the customer’s images on them unless they have some great images. Be creative; show us the feeling you are trying to portray with your image choices. Use any royalty-free site you choose. We subscribe to Kelvra and mainly use their images, but we can purchase images outside of Kelvra. PLEASE NOTE: we will not submit designs to clients with watermarks on the images.

FONTS:
We ask that you identify the fonts you’re using in the design. This can be done in a message if you want. We typically use Google Fonts and Kelvra Fonts.

CONTENT:
We're always open to different content and ideas. We often submit designs with stock images so the client can see our vision. We typically take pictures after the website launch to use their images with our vision. Lorem Ipsum is fine for paragraphs, but we ask that you make the Headers with correct English. We want to be able to show the vision and identify the sections of the website.

INSPIRATION:
We typically add a couple of links in the brief of websites we like to help you get started in your design.

REVISIONS:
We do not often ask for revisions of the designs unless we see something in the design that may not appeal to the client. If there are slight changes that we want to make, we do that in the development process.

FEEDBACK:
We rarely give feedback on designs during the design process. We are working on many website projects and do not have the time to provide feedback. We usually respond if your request is well thought out and asks specific questions, but a note asking “feedback, please” usually goes unanswered.

```html
<!DOCTYPE html>
<html lang="en">
<head>
<meta charset="utf-8">
<title>Verdale Landscape &amp; Design</title>
<link href="https://fonts.googleapis.com/css2?family=Poppins:wght@300;400;500;600;700&family=PT+Serif:ital@1&display=swap" rel="stylesheet">
<style>
:root{
  --green:#72a83f;
  --green-dark:#3f6e22;
  --green-band:#4a7a2a;
  --purple:#6b1a6c;
  --ink:#222222;
  --muted:#555555;
  --soft:#f2f1f4;
  --footer:#231f20;
  --white:#ffffff;
  --gold:#e7a11b;
}
*{margin:0;padding:0;box-sizing:border-box}
html,body{width:1200px;height:4971px;overflow:hidden}
body{position:relative;font-family:'Poppins',sans-serif;color:var(--ink);background:var(--white)}
.abs{position:absolute}
.btn{position:absolute;display:flex;align-items:center;justify-content:center;background:var(--green);color:var(--white);font-weight:600;font-size:14px;letter-spacing:.5px;border-radius:24px;text-transform:uppercase}
.photo{position:absolute}

/* nav */
.nav{top:0;left:0;width:1200px;height:77px;background:var(--white);z-index:5}
.brand{position:absolute;left:74px;top:18px;display:flex;align-items:center;gap:10px}
.brand-mark{width:14px;height:14px;border-radius:50%;background:var(--green)}
.brand-name{font-size:24px;font-weight:600;color:var(--green-dark);letter-spacing:1px}
.menu{position:absolute;left:413px;top:28px;display:flex;gap:32px;font-size:14px;color:var(--ink)}
.menu .active{color:var(--green-dark);font-weight:500}
.quote-btn{left:976px;top:19px;width:146px;height:40px}

/* hero */
.hero{top:77px;left:0;width:1200px;height:820px;background:linear-gradient(180deg,#2f5a8a 0%,#6f9a5a 28%,#3f7a2a 55%,#5a8f2e 100%)}
.hero-title{left:154px;top:200px;color:var(--white);font-size:52px;line-height:58px;font-weight:300}
.hero-title strong{font-weight:700;text-transform:uppercase}
.hero-list{left:154px;top:394px;color:var(--white);font-size:18px;list-style:none}
.hero-list li{display:flex;align-items:center;gap:12px;height:35px}
.hero-cta{left:158px;top:524px;width:201px;height:46px}
.dots{left:548px;top:618px;display:flex;gap:6px}
.dots span{width:30px;height:4px;background:rgba(255,255,255,.5)}
.dots span.on{background:var(--white)}
.hero-curve{left:0;top:640px;width:1200px;height:260px}

/* welcome */
.plant{left:174px;top:858px;width:337px;height:386px;border-radius:40% 40% 50% 50%;background:linear-gradient(160deg,#8cbd55 0%,#72a83f 50%,#6b1a6c 100%)}
.welcome-kicker{left:594px;top:897px;font-size:18px}
.welcome-title{left:594px;top:925px;font-size:30px;font-weight:400;color:var(--purple)}
.welcome-title b{font-weight:700}
.welcome-text{left:594px;top:978px;width:440px;font-size:15px;line-height:27px;color:var(--ink)}
.read-btn{left:594px;top:1160px;width:160px;height:46px}

.section-title{position:absolute;left:0;width:1200px;text-align:center;font-size:44px;font-weight:300;color:var(--ink)}
.section-title b{font-weight:700;color:var(--purple)}

/* services */
.card{position:absolute;top:1431px;width:320px;height:286px;border:8px solid var(--purple);border-top-width:6px;border-radius:0 0 160px 160px;overflow:hidden}
.card.alt{border-color:var(--green)}
.card .fill{position:absolute;inset:0}
.card span{position:absolute;left:0;width:100%;top:168px;text-align:center;color:var(--white);font-size:28px;font-weight:600}
.arrow{position:absolute;top:1514px;width:44px;height:44px;border-radius:50%;border:2px solid var(--purple);background:var(--white);display:flex;align-items:center;justify-content:center}

/* how it works */
.band{left:0;top:1790px;width:1200px;height:650px}
.how-title{top:1940px;color:var(--white)}
.how-title b{color:var(--white)}
.how-sub{left:0;width:1200px;top:2020px;text-align:center;color:#eef4e6;font-size:17px;line-height:26px}
.step{position:absolute;top:2106px;width:260px;text-align:center;color:var(--white);font-size:18px;line-height:23px}
.step-icon{margin:0 auto 20px;width:116px;height:116px;border-radius:50%;border:4px solid var(--white);background:#e9f1df;display:flex;align-items:center;justify-content:center}
.pkg-btn{left:498px;top:2336px;width:204px;height:46px}

/* work */
.work-bg{left:0;top:2440px;width:1200px;height:822px;background:var(--soft)}
.view-more{display:flex;flex-direction:column;align-items:center;justify-content:center;gap:6px;color:var(--white);font-size:20px;font-weight:600}
.learn-btn{left:525px;top:3150px;width:144px;height:42px;background:transparent;border:2px solid var(--green);color:var(--green-dark);font-size:12px}

/* solutions */
.sol-kicker{left:0;width:1200px;top:3326px;text-align:center;font-size:30px;color:var(--ink)}
.sol-title{left:0;width:1200px;top:3366px;text-align:center;font-size:32px;font-weight:700;color:var(--purple)}
.sol-photo{left:409px;top:3473px;width:366px;height:366px;border-radius:50%;border:5px solid var(--green);background:linear-gradient(180deg,#3e6a2a 0%,#5c8f36 45%,#7fb14a 100%)}
.sol-icon{position:absolute;width:90px;height:90px;border-radius:50%;background:var(--white);border:4px solid var(--green);display:flex;align-items:center;justify-content:center}
.sol-item{position:absolute;width:230px;font-size:12px;line-height:20px;color:var(--muted)}
.sol-item h3{font-size:18px;font-weight:700;color:#24324a;margin-bottom:6px}
.sol-item.right{text-align:right}

/* testimonials */
.t-line{left:530px;top:4077px;width:136px;height:2px;background:var(--green)}
.t-card{position:absolute;top:4119px;width:400px;height:231px;background:var(--white);border-radius:10px;box-shadow:0 6px 20px rgba(0,0,0,.12);text-align:center;padding:28px 34px 0}
.t-card::after{content:"";position:absolute;bottom:-30px;left:64px;border-left:0 solid transparent;border-right:40px solid transparent;border-top:30px solid var(--white)}
.t-quote{font-family:'PT Serif',serif;font-size:46px;color:#d6d6d6;line-height:30px;height:40px}
.t-text{font-family:'PT Serif',serif;font-style:italic;font-size:14.5px;line-height:21px;color:var(--muted)}
.t-stars{margin-top:14px;color:var(--gold);font-size:16px;letter-spacing:3px}
.avatar{position:absolute;top:4376px;width:84px;height:84px;border-radius:50%;background:linear-gradient(160deg,#b8c6a4,#7a6a5a)}
.t-name{position:absolute;top:4400px;font-size:11px;font-weight:600;color:var(--purple);line-height:20px;text-transform:uppercase}
.t-dots{left:545px;top:4466px;display:flex;gap:16px}
.t-dots span{width:10px;height:10px;border-radius:50%;background:#dcdcdc}
.t-dots span.on{background:var(--green)}

/* footer */
.footer-shape{left:0;top:4570px;width:1200px;height:401px}
.f-brand{left:160px;top:4686px;display:flex;align-items:center;gap:10px}
.f-brand .brand-name{color:var(--white);font-size:30px}
.f-phone{left:160px;top:4764px;color:var(--white);font-size:20px;font-weight:500}
.f-small{left:160px;color:#cfcfcf;font-size:11px}
.f-col{position:absolute;top:4694px;color:var(--white)}
.f-col h4{font-size:15px;font-weight:600;padding-bottom:6px;border-bottom:2px solid var(--green);display:inline-block;margin-bottom:20px}
.f-col ul{list-style:none;font-size:11px;color:#cfcfcf}
.f-col li{height:28px}
.social{display:flex;gap:14px;margin-top:6px}
.social span{width:18px;height:18px;border-radius:50%;border:2px solid var(--white)}
.f-rule{left:160px;top:4890px;width:876px;height:1px;background:#444}
.f-copy{left:0;width:1200px;top:4910px;text-align:center;color:#bbbbbb;font-size:12px}
</style>
</head>
<body>

<header class="nav abs">
  <div class="brand"><span class="brand-mark"></span><span class="brand-name">VERDALE</span></div>
  <nav class="menu"><span class="active">HOME</span><span>SERVICES</span><span>ABOUT</span><span>WHY US?</span><span>FAQ</span><span>CONTACT</span></nav>
  <div class="btn quote-btn">Get a Quote</div>
</header>

<section class="hero abs" role="img" aria-label="Photo of a landscaped backyard with lawn, stepping stones, palm trees and a swimming pool">
  <h1 class="hero-title abs">We Bring<br><strong>Your Landscape</strong><br>to Life</h1>
  <ul class="hero-list abs">
    <li><svg width="20" height="20" viewBox="0 0 20 20"><circle cx="10" cy="10" r="8.5" fill="none" stroke="#fff" stroke-width="1.6"/><path d="M6 10.5l3 3 5-6" fill="none" stroke="#fff" stroke-width="1.8"/></svg>15 Years Combined Experience</li>
    <li><svg width="20" height="20" viewBox="0 0 20 20"><circle cx="10" cy="10" r="8.5" fill="none" stroke="#fff" stroke-width="1.6"/><path d="M6 10.5l3 3 5-6" fill="none" stroke="#fff" stroke-width="1.8"/></svg>Custom Design</li>
    <li><svg width="20" height="20" viewBox="0 0 20 20"><circle cx="10" cy="10" r="8.5" fill="none" stroke="#fff" stroke-width="1.6"/><path d="M6 10.5l3 3 5-6" fill="none" stroke="#fff" stroke-width="1.8"/></svg>Quality that is guaranteed</li>
  </ul>
  <div class="btn hero-cta">Schedule a Call</div>
  <div class="dots abs"><span></span><span class="on"></span><span></span></div>
</section>
<svg class="hero-curve abs" viewBox="0 0 1200 260" preserveAspectRatio="none">
  <path d="M0 250 C250 60 700 20 1200 90 L1200 260 L0 260 Z" fill="#ffffff"/>
  <path d="M0 250 C250 60 700 20 1200 90" fill="none" stroke="#72a83f" stroke-width="8"/>
</svg>

<div class="plant abs" role="img" aria-label="Illustration of a green sprout growing from a purple pot"></div>
<p class="welcome-kicker abs">WELCOME TO</p>
<h2 class="welcome-title abs"><b>VERDALE</b> Landscape &amp; Design</h2>
<p class="welcome-text abs">Lorem Ipsum is simply dummy text of the printing and typesetting industry. Lorem Ipsum has been the industry's standard dummy text ever since the 1500s, when an unknown printer took a galley of type and scrambled it to make a type specimen book. It has survived not only five centuries,</p>
<div class="btn read-btn">Read More</div>

<h2 class="section-title" style="top:1330px">Our <b>Services</b></h2>
<div class="card" style="left:108px"><div class="fill" role="img" aria-label="Photo of a curved stone driveway lined with shrubs" style="background:linear-gradient(180deg,#5a7a3a,#4a4a55)"></div><span>Driveways</span></div>
<div class="card alt" style="left:440px"><div class="fill" role="img" aria-label="Photo of a paver walkway with flower beds" style="background:linear-gradient(180deg,#6f8a4a,#7a6a5e)"></div><span>Pavers</span></div>
<div class="card" style="left:770px"><div class="fill" role="img" aria-label="Photo of a modern house with a fenced front yard" style="background:linear-gradient(180deg,#5d8cc8,#8a8a88 55%,#4f7a34)"></div><span>Fences</span></div>
<div class="arrow" style="left:82px"><svg width="14" height="14" viewBox="0 0 14 14"><path d="M9 2L4 7l5 5" fill="none" stroke="#6b1a6c" stroke-width="2"/></svg></div>
<div class="arrow" style="left:1070px"><svg width="14" height="14" viewBox="0 0 14 14"><path d="M5 2l5 5-5 5" fill="none" stroke="#6b1a6c" stroke-width="2"/></svg></div>

<svg class="band abs" viewBox="0 0 1200 650" preserveAspectRatio="none" role="img" aria-label="Green tinted photo of a garden pergola">
  <path d="M0 110 L1200 0 L1200 650 L0 650 Z" fill="#4a7a2a"/>
</svg>
<h2 class="section-title how-title">HOW IT <b>WORKS?</b></h2>
<p class="how-sub abs">We understand how important your home is to you and work wirth you<br>to ensure you get the results you want.</p>
<div class="step" style="left:182px"><div class="step-icon"><svg width="60" height="60" viewBox="0 0 60 60"><circle cx="30" cy="30" r="24" fill="#72a83f"/><path d="M12 38c10-6 26-6 36 0" stroke="#fff" stroke-width="3" fill="none"/></svg></div>Share, Plan,<br>and Budget</div>
<div class="step" style="left:474px"><div class="step-icon"><svg width="60" height="60" viewBox="0 0 60 60"><circle cx="30" cy="30" r="24" fill="#72a83f"/><rect x="16" y="24" width="28" height="6" fill="#fff"/><path d="M20 30v12M40 30v12" stroke="#fff" stroke-width="3"/></svg></div>REVIEW, COLLABORATE,<br>AND ITERATE</div>
<div class="step" style="left:752px"><div class="step-icon"><svg width="60" height="60" viewBox="0 0 60 60"><circle cx="30" cy="30" r="24" fill="#72a83f"/><circle cx="24" cy="28" r="7" fill="#fff"/><circle cx="36" cy="28" r="7" fill="#fff"/><path d="M14 42h32" stroke="#fff" stroke-width="3"/></svg></div>Finalize design</div>
<div class="btn pkg-btn">Design Packages</div>

<div class="work-bg abs"></div>
<h2 class="section-title" style="top:2497px">Latest <b>Work</b></h2>
<div class="photo" role="img" aria-label="Photo of a deck chair on a lawn beside a wooden fence" style="left:160px;top:2585px;width:432px;height:255px;background:linear-gradient(180deg,#4a5a34,#6a9a3a)"></div>
<div class="photo view-more" role="img" aria-label="Photo of a stepping stone path under a purple overlay" style="left:604px;top:2585px;width:432px;height:255px;background:linear-gradient(180deg,#7a3f82,#9a5fa0)">
  <svg width="34" height="34" viewBox="0 0 34 34"><circle cx="14" cy="14" r="10" fill="none" stroke="#fff" stroke-width="3"/><path d="M21 21l9 9" stroke="#fff" stroke-width="3"/></svg>View More</div>
<div class="photo" role="img" aria-label="Photo of a stone path through tropical plants" style="left:160px;top:2851px;width:284px;height:255px;background:linear-gradient(180deg,#3e6a2a,#8a9a7a)"></div>
<div class="photo" role="img" aria-label="Photo of a wooden bench beside a garden walkway" style="left:456px;top:2851px;width:284px;height:255px;background:linear-gradient(180deg,#5f8f3a,#7a7a70)"></div>
<div class="photo" role="img" aria-label="Photo of a front yard with landscaped beds and a house" style="left:752px;top:2851px;width:284px;height:255px;background:linear-gradient(180deg,#7a7a80,#5f8f34)"></div>
<div class="btn learn-btn">Learn More</div>

<p class="sol-kicker abs">WE PROVIDE</p>
<h2 class="sol-title abs">CUSTOM SOLUTIONS TO CLIENT NEEDS</h2>
<div class="sol-photo abs" role="img" aria-label="Photo of two white lawn chairs on grass"></div>
<div class="sol-icon" style="left:426px;top:3466px"><svg width="46" height="46" viewBox="0 0 46 46"><path d="M6 34l12-14 8 8 6-6 8 12" fill="none" stroke="#6b1a6c" stroke-width="2.5"/></svg></div>
<div class="sol-icon" style="left:723px;top:3597px"><svg width="46" height="46" viewBox="0 0 46 46"><circle cx="16" cy="20" r="8" fill="none" stroke="#6b1a6c" stroke-width="2.5"/><circle cx="30" cy="20" r="8" fill="none" stroke="#6b1a6c" stroke-width="2.5"/><path d="M16 28v10M30 28v10" stroke="#6b1a6c" stroke-width="2.5"/></svg></div>
<div class="sol-icon" style="left:462px;top:3769px"><svg width="46" height="46" viewBox="0 0 46 46"><path d="M12 38L32 10M20 36l18-18" stroke="#6b1a6c" stroke-width="2.5"/></svg></div>
<div class="sol-item right" style="left:167px;top:3462px"><h3>INSTALLATION</h3>Lorem Ipsum is simply dummy<br>text of the printing typesetting<br>Lorem Ipsum has been</div>
<div class="sol-item" style="left:835px;top:3598px"><h3>CUSTOM SOLUTIONS</h3>Lorem Ipsum is simply dummy<br>text of the printing typesetting<br>Lorem Ipsum has been</div>
<div class="sol-item right" style="left:198px;top:3780px"><h3>MAINTENANCE</h3>Lorem Ipsum is simply dummy<br>text of the printing typesetting<br>Lorem Ipsum has been</div>

<h2 class="section-title" style="top:4006px;font-size:38px">What Our <b style="color:var(--ink)">Customers Say</b></h2>
<div class="t-line abs"></div>
<div class="t-card" style="left:180px"><div class="t-quote">&rdquo;</div><p class="t-text">Sed ut perspiciatis unde omnis iste natus error sit voluptatem accntium doloremque laudantium, totam rem aperiam, eaque ipsa quae ab illo intore veritatis et quasi architecto beatae vitae dicta sunt explicabo. Nemo enim ipsam voluptatem</p><div class="t-stars">★★★★★</div></div>
<div class="t-card" style="left:614px"><div class="t-quote">&rdquo;</div><p class="t-text">Sed ut perspiciatis unde omnis iste natus error sit voluptatem accntium doloremque laudantium, totam rem aperiam, eaque ipsa quae ab illo intore veritatis et quasi architecto beatae vitae dicta sunt explicabo. Nemo enim ipsam voluptatem</p><div class="t-stars">★★★★★</div></div>
<div class="avatar" style="left:309px" role="img" aria-label="Customer portrait"></div>
<div class="t-name" style="left:405px">Ezra Vantell<br>Fernlight Studio</div>
<div class="avatar" style="left:744px" role="img" aria-label="Customer portrait"></div>
<div class="t-name" style="left:840px">Mira Quell<br>Fernlight Studio</div>
<div class="t-dots abs"><span></span><span></span><span class="on"></span><span></span><span></span></div>

<svg class="footer-shape abs" viewBox="0 0 1200 401" preserveAspectRatio="none">
  <path d="M0 50 C300 0 800 -10 1200 80 L1200 401 L0 401 Z" fill="#231f20"/>
  <path d="M0 50 C300 0 800 -10 1200 80 L1200 40 C800 -30 300 -20 0 50 Z" fill="#72a83f"/>
</svg>
<div class="f-brand abs"><span class="brand-mark"></span><span class="brand-name">VERDALE</span></div>
<p class="f-phone abs">0 (800) 555 0142</p>
<p class="f-small abs" style="top:4805px">hello@verdale.example</p>
<p class="f-small abs" style="top:4826px">18 Brambleway Lane, Alderidge</p>
<div class="f-col" style="left:423px"><h4>Services</h4><ul><li>Residential</li><li>Commercial</li><li>Patios &amp; Decks</li></ul></div>
<div class="f-col" style="left:610px"><h4>Footer Links</h4><ul><li style="height:24px">About Us</li><li style="height:24px">Why Us?</li><li style="height:24px">FAQ</li><li style="height:24px">Contact Us</li></ul></div>
<div class="f-col" style="left:814px"><h4>Social</h4><div class="social"><span></span><span></span><span></span><span></span><span></span></div></div>
<div class="f-rule abs"></div>
<p class="f-copy abs">Copyright 2023 © Verdale. All Right Reserved.</p>

</body>
</html>
```